TAVRO Capital Group LLC a High Risk Big Rewards company for Rich Young Entrepreneurs

We would like a very modern, powerful in the eyes of our customers, modern, minimalist feel, financial gain. this business card is for young Rich entrepreneurs who want to invest money into High Risk, Big Rewards Businesses. The card Should sell the business!! let your creativity go Wild! I pick most of the designers for this project because of your BOLD Designs, I would like this card to be Bold, Modern, Minimalist, use as many effects in your graphic Artist Mind, Do not let the Financial sound of this business to make you think Conservative that's the last thing we are! if you have a lot of money and you want to play a risky market call US
Updates

Project Deadline Extended
Reason: have not received, enough designs to choose 1st and second place, sure I have received over 100 designs but it seems most designers are submitting every card they have ever made before and calling it mine, please we are looking for fresh ideas please!

Target Market(s)

Private Risky Investors

Industry/Entity Type

Financial

Contact Information for Business Card

powerful in the eyes of our customers,modern, minimalist feel

Font styles to use
Other font styles liked:
• Modern feeling fonts

Requirements
Must have
• The Company Name is TAVRO Capital Group LLC and it must be on the CARD
• My Name, title, Cell , email
• Delvin Ashcroft G.E.D.
• Managing Member
• 555.038.6195
• delvin@tavrocapitalgroup.example
Nice to have
• try a black thick plastic card with round corners with Delvin Ashcroft GED (make sure GED is smaller than name) just on one side of the card, and my phone number with out the icons and email on the other side, this card should look like a exclusive credit card or exclusive VIP card, something you would never loose

```html
<!DOCTYPE html>
<html lang="en">
<head>
<meta charset="utf-8">
<title>TAVRO Capital Group LLC – Business Card</title>
<link rel="stylesheet" href="https://fonts.googleapis.com/css2?family=Open+Sans:wght@400;600;700&display=swap">
<style>
  :root {
    --page-bg: #d9d6d2;
    --card-top: #eef0f2;
    --card-bottom: #dfe2e5;
    --card-edge: #8d9297;
    --brand-blue: #1f6fc4;
    --blue-light: #1a9be0;
    --blue-deep: #2541a8;
    --band-dark: #262a2f;
    --silver: #e4e8ec;
    --text-grey: #3c3f43;
  }
  * { margin: 0; padding: 0; box-sizing: border-box; }
  html, body {
    width: 1200px;
    height: 970px;
    overflow: hidden;
    background: var(--page-bg);
    font-family: "Open Sans", Arial, sans-serif;
  }
  .business-card {
    position: absolute;
    left: 80px;
    top: 195px;
    width: 1040px;
    height: 580px;
    border-radius: 26px;
    overflow: hidden;
    background: linear-gradient(160deg, var(--card-top), var(--card-bottom));
    border: 2px solid var(--card-edge);
    box-shadow: 0 10px 30px rgba(0, 0, 0, 0.18);
  }
  .card-swoosh {
    position: absolute;
    inset: 0;
    width: 100%;
    height: 100%;
  }
  .company-name {
    position: absolute;
    left: 66px;
    top: 150px;
    font-size: 32px;
    font-weight: 700;
    color: var(--brand-blue);
    letter-spacing: 0.2px;
  }
  .edge-tab {
    position: absolute;
    left: -34px;
    top: 330px;
    width: 68px;
    height: 86px;
    border-radius: 50%;
    background: var(--brand-blue);
  }
  .holder-name {
    position: absolute;
    left: 66px;
    top: 342px;
    font-size: 29px;
    font-weight: 400;
    color: var(--brand-blue);
  }
  .holder-name .credential { margin-left: 10px; }
  .holder-title {
    position: absolute;
    left: 66px;
    top: 384px;
    font-size: 21px;
    color: var(--text-grey);
  }
  .contact-list {
    position: absolute;
    left: 66px;
    top: 454px;
    list-style: none;
  }
  .contact-item {
    display: flex;
    align-items: center;
    gap: 12px;
    font-size: 21px;
    color: var(--text-grey);
    height: 34px;
  }
  .contact-icon { width: 20px; height: 20px; flex: none; }
</style>
</head>
<body>
  <div class="business-card">
    <svg class="card-swoosh" viewBox="0 0 755 420" preserveAspectRatio="none" aria-hidden="true">
      <defs>
        <linearGradient id="blueFill" x1="0" y1="0" x2="0.3" y2="1">
          <stop offset="0" stop-color="var(--blue-light)"/>
          <stop offset="1" stop-color="var(--blue-deep)"/>
        </linearGradient>
      </defs>
      <path d="M485,0 L755,0 L755,420 L712,420 Q690,150 485,0 Z" fill="url(#blueFill)"/>
      <path d="M443,0 Q600,150 623,420 L704,420 Q682,150 478,0 Z" fill="var(--band-dark)"/>
      <path d="M480,0 Q685,150 708,420" fill="none" stroke="var(--silver)" stroke-width="4"/>
    </svg>

    <div class="company-name">TAVRO Capital Group LLC</div>

    <div class="edge-tab"></div>

    <div class="holder-name">Delvin Ashcroft<span class="credential">G.E.D</span></div>
    <div class="holder-title">Managing Member</div>

    <ul class="contact-list">
      <li class="contact-item">
        <svg class="contact-icon" viewBox="0 0 20 20" aria-hidden="true">
          <rect x="5" y="1" width="10" height="18" rx="2" fill="none" stroke="var(--text-grey)" stroke-width="2"/>
          <rect x="7.5" y="4" width="5" height="6" fill="var(--text-grey)"/>
          <circle cx="10" cy="15" r="1.4" fill="var(--text-grey)"/>
        </svg>
        <span>555.038.6195</span>
      </li>
      <li class="contact-item">
        <svg class="contact-icon" viewBox="0 0 20 20" aria-hidden="true">
          <rect x="1" y="4" width="18" height="12" fill="var(--text-grey)"/>
          <path d="M1.5,4.5 L10,11 L18.5,4.5" fill="none" stroke="var(--card-top)" stroke-width="1.6"/>
        </svg>
        <span>delvin@tavrocapitalgroup.example</span>
      </li>
    </ul>
  </div>
</body>
</html>
```